Premium Personal Brand — Facebook Banner (Used Across All Platforms)

Update — Additional Color Direction
In addition to the dark charcoal/slate direction already described, I'm also interested in seeing variants with:
Dark navy blue — Deep, authoritative, intelligence-community feel. Same textured/matte treatment, not flat or bright.
Warm charcoal with steel blue accent — Keep the dark base but introduce a subtle steel blue gradient, accent line, or tonal shift. Sophisticated, modern, adds dimension without adding color noise.
Both should maintain the same premium, restrained, architectural feel described in the original brief. No bright blues, no corporate PowerPoint energy — think midnight, think depth, think weight.
Everything else in the brief remains the same.
I am building a premium personal brand as an executive advisor to founders ($5M+ revenue).
This contest is Facebook-banner–focused, but the design must represent a visual system that will be reused across:
- LinkedIn
- YouTube
I- nstagram
- X (Twitter)
- Website hero sections and other brand touchpoints
Think of the Facebook banner as the primary expression of the brand — not a one-off graphic.
This project is about discovering a high-end visual style and brand feel, not decoration.
What to design
Please submit one cohesive visual system, shown primarily as:
- Facebook banner (primary focus)
The same design language should clearly translate to all platforms listed above.
Designers are responsible for using the current recommended dimensions for each platform.
Quick clarification on background direction:
Backgrounds should have depth and texture, not flat color fields. Avoid pure white, light grey, or solid black backgrounds. Think matte, architectural materials — stone, graphite, concrete, steel — not blank canvases. Subtle tonal variation is encouraged. Obvious gradients or decorative patterns are not.
Text to use
Primary Headline:
- Your Business Is Too Valuable To Be Run On Hope.
Subheadline:
- You didn’t build a business to become its prisoner.
Name:
Paul Whitaker
The headline should be the dominant visual element.
Logo note (important)
My personal logo is currently being finalized.
For this contest:
- Use a simple “PW” monogram placeholder
- Clean, bold, geometric sans-serif
- Do not design a logo
- The winning design must allow an easy logo swap later.
Headshot note (important)
- Please do not include a headshot in the banner design.
- Most platforms display a circular profile image separately.
- The banner should stand on its own using typography, layout, and tone only.
- Design the banner assuming the profile photo will sit nearby, not inside the banner.
Style direction
The design should feel:
- Premium
- Calm
- Confident
- Restrained
- High-trust
- Dark, neutral backgrounds are preferred.
- Fewer elements are better than more.
Think:
- Owner-level advisor
- Private equity / boardroom tone
- Industrial, Modern, Minimalist, Elite, Architectural, not decorative
What to avoid
Please do not submit designs that feel:
- Promotional, hype-driven, or salesy
- Like a coach, guru, or agency
- Bright, colorful, or gradient-heavy
- Busy or over-designed
- Based on stock photos
- No motivational speaker energy.
Reaction test
- If someone sees this banner on Facebook (or later on LinkedIn, YouTube, etc.), the reaction should be:
“That person is serious. I’d trust them with important decisions.”
Final note
- I am not looking for many variations.
- I am looking for one strong visual direction you believe in.
Simple beats clever.
- Restraint beats decoration.

```html
<!DOCTYPE html>
<html lang="en">
<head>
<meta charset="UTF-8">
<title>Paul Whitaker — Banner</title>
<link href="https://fonts.googleapis.com/css2?family=Inter+Tight:wght@400;500;700&display=swap" rel="stylesheet">
<style>
  :root {
    --navy-deep: #0a1320;
    --navy-mid: #13233a;
    --text-white: #ffffff;
    --text-soft: #e3e8ef;
    --rule: rgba(150, 175, 205, 0.35);
  }
  * { margin: 0; padding: 0; box-sizing: border-box; }
  html, body {
    width: 1200px;
    height: 527px;
    overflow: hidden;
    background: var(--navy-deep);
  }
  .banner {
    position: relative;
    width: 1200px;
    height: 527px;
    overflow: hidden;
    font-family: "Inter Tight", Arial, sans-serif;
    color: var(--text-white);
    background:
      radial-gradient(ellipse 70% 90% at 30% 40%, rgba(40, 66, 96, 0.55), transparent 70%),
      radial-gradient(ellipse 60% 80% at 85% 90%, rgba(4, 9, 16, 0.7), transparent 70%),
      linear-gradient(135deg, var(--navy-mid) 0%, var(--navy-deep) 100%);
  }
  .facet {
    position: absolute;
    inset: 0;
    width: 100%;
    height: 100%;
  }
  .headline {
    position: absolute;
    top: 114px;
    left: 0;
    width: 100%;
    text-align: center;
    font-weight: 700;
    font-size: 51px;
    line-height: 55px;
    letter-spacing: -0.2px;
  }
  .subheadline {
    position: absolute;
    top: 266px;
    left: 0;
    width: 100%;
    text-align: center;
    font-weight: 400;
    font-size: 18px;
    letter-spacing: 0.6px;
    text-transform: uppercase;
    color: var(--text-soft);
  }
  .subheadline-rule {
    position: absolute;
    top: 298px;
    left: 440px;
    width: 320px;
    height: 1px;
    background: linear-gradient(90deg, transparent, var(--rule) 20%, var(--rule) 80%, transparent);
  }
  .initials {
    position: absolute;
    top: 388px;
    left: 0;
    width: 100%;
    text-align: center;
    font-weight: 500;
    font-size: 30px;
    line-height: 40px;
    letter-spacing: 1px;
  }
  .name {
    position: absolute;
    top: 457px;
    left: 0;
    width: 100%;
    text-align: center;
    font-weight: 500;
    font-size: 20px;
    letter-spacing: 0.8px;
    text-transform: uppercase;
  }
</style>
</head>
<body>
  <div class="banner">
    <svg class="facet" viewBox="0 0 1200 527" preserveAspectRatio="none" aria-hidden="true">
      <defs>
        <linearGradient id="facetLight" x1="0" y1="0" x2="1" y2="1">
          <stop offset="0" stop-color="#2a4260" stop-opacity="0.35"/>
          <stop offset="1" stop-color="#2a4260" stop-opacity="0"/>
        </linearGradient>
      </defs>
      <polygon points="0,0 500,0 70,527 0,527" fill="url(#facetLight)"/>
    </svg>

    <h1 class="headline">Your Business Is Too Valuable<br>To Be Run On Hope</h1>
    <p class="subheadline">You didn’t build a business to become its prisoner</p>
    <div class="subheadline-rule"></div>

    <p class="initials">PW</p>
    <p class="name">Paul Whitaker</p>
  </div>
</body>
</html>
```